Flyer creation for holiday food gift programs

1. Flyer Background (sample of last years flyer is attached)a. Purpose – to promote holiday food gift businessb. Where is it used - We feature this flyer on our website for our customer (distributors) to download print and or email to their clients.c. Customers (distributors) have the option to put their logo and contact info on the bottom portion of the flyer, (as to why the bottom 2.5 inches is empty/or faded).d. Our customers (distributors) use this flyer to market to their clients (end-buyers) how food gifts.1. They email or print it off and hand it out.2. They send it to current end-buyers and new end-buyerse. I have attached 6 images to use without their background,, please use the three that best fit your layout. I was only able to upload jpgs. I can send the hi res when you know which one you want to use.1. Item# KM407 from $39 to $662. Item#SVL582 from $14 to $243. Item#MQA8264 from $44 to $674. Item#DWF6142 from $69 to $2495. Item#PZH937 from $24 to $496. Item#J8463 from $62 to $99f. The call to action is to get the end-buyer to contact the customer (distributor)g. The below can also be used in bullets, the first being a headline.1. Achieve the most from your business gifting! or Make Gift-Giving Unforgettable!2. Your logo on every gift3. Stress free gift giving4. Delicious Gifts they’ll remember and enjoy.5. Your one stop shop6. Gifts to fit every price pointh. If you have any questions, please feel free to email us. You can view our website for a better feel of our products and you can also view our white paper to understand our background, see attached.

Target Market(s)

Corporations that purchase holiday gifts for their employees and customers.

Requirements
Nice to have
• Elegant design and a holiday look
Should not have
• Green usually doesn't work well with food. No Christmas trees.

```html
<!DOCTYPE html>
<html lang="en">
<head>
<meta charset="UTF-8">
<title>Business Gifting Flyer</title>
<link href="https://fonts.googleapis.com/css2?family=Bebas+Neue&family=Montserrat:wght@600&family=Oswald:wght@400;500;600&family=Pinyon+Script&family=Playfair+Display:ital,wght@1,400&display=swap" rel="stylesheet">
<style>
  :root{
    --wine:#7c1d24;
    --wine-dark:#6e161d;
    --amber:#f6a93b;
    --bullet-text:#f9c25a;
    --beige:#e3d8cc;
    --sage:#8fa283;
    --lavender:#a08ca8;
    --lavender-text:#6d5a78;
    --taupe:#a88b6e;
    --taupe-text:#7d5f45;
    --ink:#1d1d1d;
    --white:#ffffff;
  }
  *{margin:0;padding:0;box-sizing:border-box}
  html,body{width:887px;height:1200px;overflow:hidden;background:var(--white)}
  .flyer{position:relative;width:887px;height:1200px;overflow:hidden;background:var(--white);font-family:'Oswald',sans-serif}
  .hero-bg{position:absolute;left:0;top:0;width:887px;height:500px;background:linear-gradient(90deg,#d9cdc1 0%,var(--beige) 55%,#e8dfd6 100%)}
  .hero-photo{position:absolute;left:0;top:0;width:520px;height:470px;
    background:radial-gradient(ellipse at 40% 30%,#d4a24a 0%,#c8943f 14%,#d98f6e 26%,#e7c3ac 42%,rgba(227,216,204,0) 72%)}
  .curves{position:absolute;left:0;top:0}
  .headline{position:absolute;right:19px;top:44px;text-align:right;color:var(--wine);font-family:'Bebas Neue',sans-serif;line-height:1}
  .headline .lead{display:block;font-size:41px;letter-spacing:.2px}
  .headline .main{display:block;font-size:82px;margin-top:2px;letter-spacing:.5px}
  .product-shot{position:absolute;border-radius:14px}
  .shot-chocolate{left:120px;top:416px;width:328px;height:184px;background:radial-gradient(ellipse at 55% 55%,#5a3220 0%,#8a5a3b 35%,#e9dcc6 62%,rgba(255,255,255,0) 80%)}
  .shot-tower{left:544px;top:248px;width:304px;height:280px;background:radial-gradient(ellipse at 50% 55%,#2a2f52 0%,#8a6a3e 35%,#e5d6b8 60%,rgba(255,255,255,0) 80%)}
  .shot-cheese{left:544px;top:664px;width:308px;height:232px;background:radial-gradient(ellipse at 50% 55%,#2b2b2b 0%,#f2c14e 30%,#e8d9c0 58%,rgba(255,255,255,0) 80%)}
  .price-tag{position:absolute;height:46px;border:1.5px solid;border-radius:0 24px 24px 0;background:var(--white);display:flex;align-items:center;padding-left:46px;white-space:nowrap}
  .price-tag .word{font-family:'Pinyon Script',cursive;font-size:22px;margin:0 4px}
  .price-tag .amount{font-family:'Playfair Display',serif;font-style:italic;font-size:36px;line-height:1}
  .price-tag .amount small{font-size:20px}
  .badge{position:absolute;width:120px;height:120px;border-radius:50%;display:flex;align-items:center;justify-content:center;text-align:center;color:var(--white);font-family:'Montserrat',sans-serif;font-weight:600;font-size:16.5px;line-height:1.45}
  .tag-chocolate{left:160px;top:622px;width:258px;border-color:var(--sage);color:#5f7553;padding-left:28px}
  .badge-chocolate{left:64px;top:586px;background:var(--sage)}
  .tag-tower{left:596px;top:534px;width:264px;border-color:var(--lavender);color:var(--lavender-text);padding-left:14px}
  .badge-tower{left:480px;top:498px;background:var(--lavender)}
  .tag-cheese{left:616px;top:912px;width:238px;border-color:var(--taupe);color:var(--taupe-text);padding-left:12px}
  .badge-cheese{left:498px;top:878px;background:var(--taupe)}
  .benefits{position:absolute;left:29px;top:750px;list-style:none}
  .benefits li{height:32px;margin-bottom:11px;background:var(--wine);border-left:5px solid var(--amber);color:var(--bullet-text);font-size:19px;font-weight:500;line-height:32px;padding-left:18px;clip-path:polygon(0 0,calc(100% - 22px) 0,100% 100%,0 100%)}
  .footer-band{position:absolute;left:0;top:1044px;width:887px;height:128px;background:linear-gradient(90deg,#ffffff 0%,#ffffff 45%,#eee4dc 75%,#c9b09c 100%)}
  .distributor{position:absolute;left:40px;top:1050px;width:456px;text-align:center;color:var(--ink)}
  .distributor .label{font-size:19px;font-weight:500;line-height:1}
  .distributor .logo-slot{font-size:50px;font-weight:500;line-height:1;margin-top:6px;padding-bottom:8px;border-bottom:1px solid var(--ink)}
  .distributor .address{font-size:15px;margin-top:4px;font-weight:400}
  .contact{position:absolute;left:566px;top:1062px;color:var(--ink);font-size:17px;line-height:1}
  .contact .intro{font-weight:500;font-size:18px}
  .contact p{margin-bottom:9px}
  .contact .phone{font-size:25px;font-weight:600;margin-left:6px}
  .contact .email{font-size:24px;font-weight:600}
</style>
</head>
<body>
<div class="flyer">
  <div class="hero-bg"></div>
  <div class="hero-photo" role="img" aria-label="Hands holding out a gold gift box tied with a red ribbon"></div>

  <svg class="curves" width="887" height="1200" viewBox="0 0 887 1200" aria-hidden="true">
    <path d="M0,490 C200,330 450,240 887,228 L887,1200 L0,1200 Z" fill="#ffffff"/>
    <path d="M0,440 C180,300 450,215 887,210 L887,222 C450,232 200,320 0,478 Z" fill="var(--wine)"/>
    <path d="M0,478 C200,320 450,232 887,222 L887,228 C450,240 200,330 0,490 Z" fill="var(--amber)"/>
  </svg>

  <h1 class="headline">
    <span class="lead">Achieve the most from your</span>
    <span class="main">Business Gifting!</span>
  </h1>

  <div class="product-shot shot-tower" role="img" aria-label="Stacked gift tower of boxes with navy ribbon, caramel popcorn, chocolates, nuts and cookies"></div>
  <div class="price-tag tag-tower"><span class="word">from</span><span class="amount"><small>$</small>69</span><span class="word">to</span><span class="amount"><small>$</small>249</span></div>
  <div class="badge badge-tower">Gourmet<br>Gift<br>Tower</div>

  <div class="product-shot shot-chocolate" role="img" aria-label="Wooden crate of gourmet chocolates, toffee and chocolate-covered nuts"></div>
  <div class="price-tag tag-chocolate"><span class="word">from</span><span class="amount"><small>$</small>44</span><span class="word">to</span><span class="amount"><small>$</small>67</span></div>
  <div class="badge badge-chocolate">Gourmet<br>Chocolate<br>Tower</div>

  <div class="product-shot shot-cheese" role="img" aria-label="Slate board with cheeses, summer sausage, crackers and a knife"></div>
  <div class="price-tag tag-cheese"><span class="word">from</span><span class="amount"><small>$</small>62</span><span class="word">to</span><span class="amount"><small>$</small>99</span></div>
  <div class="badge badge-cheese">Gourmet<br>Gift<br>Tower</div>

  <ul class="benefits">
    <li style="width:262px">Your logo on every gift</li>
    <li style="width:231px">Stress free gift giving</li>
    <li style="width:415px">Delicious Gifts they’ll remember and enjoy.</li>
    <li style="width:209px">Your one stop shop</li>
    <li style="width:287px">Gifts to fit every price point</li>
  </ul>

  <div class="footer-band"></div>
  <div class="distributor">
    <div class="label">Distributor’s</div>
    <div class="logo-slot">LOGO</div>
    <div class="address">&amp; Address line will be here</div>
  </div>
  <div class="contact">
    <p class="intro">To know about other products :</p>
    <p>Call us Today <span class="phone">+000 000 000</span></p>
    <p>or Mail : <span class="email">info@mail.com</span></p>
  </div>
</div>
</body>
</html>
```